business card for Your Loan Scout

Please create a business card for my new business. I have attached another business card i have used previously and I like its layout and the hologram style backing with the logo. Replace the information with my new business information. On the information side of the card under the logo please place the TLCA acredited member logo I have uploaded along with 'Credit Rep Number 381749'.
next to my name in smaller text and not bold write 'JP'. and my title change from director to Broker/Director
Industry/Entity Type
Mortgage Brokerage
Contact Information for Business Card
As already on the uploaded card and in project description
Colors
Designer to choose colors to be used in the design.
Look and feel
Each slider illustrates characteristics of the customer's brand and the style your logo design should communicate.

```html
<!DOCTYPE html>
<html lang="en">
<head>
<meta charset="utf-8">
<title>Your Loan Scout – Business Card</title>
<link rel="stylesheet" href="https://fonts.googleapis.com/css2?family=Lato:wght@400;700&display=swap">
<style>
  :root {
    --backdrop: #5f7f88;
    --card: #ffffff;
    --brand-blue: #0b78c1;
    --brand-grey: #7d8d9c;
    --ink: #333333;
  }
  * { margin: 0; padding: 0; box-sizing: border-box; }
  html, body {
    width: 1200px; height: 1200px; overflow: hidden;
    background: var(--backdrop);
    font-family: "Lato", sans-serif;
    color: var(--ink);
  }
  .card {
    position: absolute; left: 180px; width: 840px; height: 480px;
    background: var(--card);
  }
  .card--front { top: 82px; }
  .card--back { top: 638px; }

  .brand {
    position: absolute; display: flex; align-items: center; gap: 12px;
    font-weight: 700; color: var(--brand-blue); white-space: nowrap;
  }
  .brand__mark { background: var(--brand-grey); flex: none; }

  .card--front .brand {
    left: 0; right: 0; top: 200px; justify-content: center; font-size: 40px;
  }
  .card--front .brand__mark { width: 40px; height: 40px; }
  .front__url {
    position: absolute; left: 0; right: 0; top: 424px;
    text-align: center; font-size: 22px; letter-spacing: 0.36em;
  }

  .card--back .brand { left: 42px; top: 66px; font-size: 26px; }
  .card--back .brand__mark { width: 26px; height: 26px; }

  .accreditation {
    position: absolute; left: 42px; top: 118px;
    display: flex; align-items: center; gap: 12px;
    font-size: 15px; white-space: nowrap;
  }
  .accreditation__badge {
    width: 38px; height: 38px; border-radius: 50%;
    background: var(--brand-grey); flex: none;
  }

  .person { position: absolute; right: 48px; top: 200px; text-align: right; }
  .person__name { font-size: 29px; font-weight: 700; color: var(--brand-blue); line-height: 1.1; }
  .person__post { font-size: 18px; font-weight: 400; }
  .person__title { font-size: 19px; margin-top: 2px; }
  .divider {
    position: absolute; left: 42px; right: 48px; top: 266px;
    height: 2px; background: var(--brand-blue);
  }
  .contacts { position: absolute; left: 42px; top: 316px; list-style: none; }
  .contacts li {
    display: flex; align-items: center; gap: 14px;
    font-size: 19px; height: 35px;
  }
  .contacts svg { width: 26px; height: 22px; flex: none; }
  .band {
    position: absolute; left: 0; right: 0; bottom: 0; height: 27px;
    background: var(--brand-blue);
  }
</style>
</head>
<body>
  <section class="card card--front">
    <div class="brand"><span class="brand__mark"></span>Your Loan Scout</div>
    <p class="front__url">yourloanscout.com.au</p>
  </section>

  <section class="card card--back">
    <div class="brand"><span class="brand__mark"></span>Your Loan Scout</div>
    <div class="accreditation">
      <span class="accreditation__badge" role="img" aria-label="TLCA accredited member badge"></span>
      Credit Rep Number 381749
    </div>
    <div class="person">
      <p class="person__name">Daniel Whitford <span class="person__post">JP</span></p>
      <p class="person__title">Broker/Director</p>
    </div>
    <div class="divider"></div>
    <ul class="contacts">
      <li>
        <svg viewBox="0 0 26 22" aria-hidden="true"><path d="M1 7c0-3 5-5 12-5s12 2 12 5v2h-6V6H7v3H1z" fill="#333"/><path d="M5 11h16l2 9H3z" fill="#333"/><circle cx="13" cy="15" r="3" fill="#fff"/></svg>
        0400 517 283
      </li>
      <li>
        <svg viewBox="0 0 26 22" aria-hidden="true"><rect x="1" y="3" width="24" height="16" fill="#333"/><path d="M1 3l12 9 12-9M1 19l9-8M25 19l-9-8" stroke="#fff" stroke-width="1.5" fill="none"/></svg>
        dan@yourloanscout.com.au
      </li>
      <li>
        <svg viewBox="0 0 26 22" aria-hidden="true" fill="none" stroke="#333" stroke-width="1.3"><circle cx="13" cy="11" r="10"/><ellipse cx="13" cy="11" rx="4.5" ry="10"/><path d="M3 11h20M4.5 6h17M4.5 16h17M13 1v20"/></svg>
        www.yourloanscout.com.au
      </li>
    </ul>
    <div class="band"></div>
  </section>
</body>
</html>
```